A5 Patient Information Booklet (Chiropractic Clinic) 4-8 pages

Here’s a polished, professional rewrite of your full brief and content, with clearer structure, corrected language, and a premium tone:

---

**Project Title:** Premium Patient Information Brochure (Chiropractic & Wellness Clinic)

---

### **Overview**

We are a health and wellness clinic seeking a premium, high-end patient information brochure to provide following a patient’s initial consultation and first treatment.

The purpose of this booklet is to:

* Reinforce trust and professionalism
* Help patients understand what to expect next
* Encourage adherence to care recommendations
* Position the clinic as calm, expert-led, and results-driven

---

### **Format**

* 4–8 page booklet (A5 or similar size)
* Print-ready and digital versions required

---

### **Target Audience**

Patients who have just completed their initial consultation and may have begun treatment. They may already be experiencing physical or mental changes, so the brochure should guide, reassure, and educate them on what comes next.

---

### **Tone & Style**

* Premium, calm, and reassuring
* Modern wellness aesthetic (not overly clinical)
* Clean layout with minimal clutter
* Soft, neutral colour palette (whites, creams, muted greens, soft blues)
* Elegant typography (e.g. Montserrat / Lato)
* High-end, trustworthy, and professional feel

---

### **Key Messages**

#### 1. Listen to Your Body

Patients may feel different after treatment. Reassure them that this is normal and part of the healing process.

#### 2. Post-Treatment Advice

* Stay well hydrated
* Rest if needed
* Avoid overexertion if the body requires recovery

#### 3. Healing is a Journey (Core Concept)

A strong visual metaphor of a **“road to recovery”** or **journey** should be central to the design.

This journey should clearly illustrate three phases:

* **Phase 1: Initial Care (Weeks 1–6)**
Focus: Reducing pain/discomfort, calming the body, and initiating response to treatment

* **Phase 2: Corrective Care (Weeks 6–12)**
Focus: Addressing underlying issues, improving function, and creating lasting change

* **Phase 3: Wellness / Maintenance (Ongoing)**
Focus: Maintaining progress, preventing relapse, and supporting long-term wellbeing

**Important:**

* Emphasise that this is not a quick fix
* Progress requires time and consistency
* Each patient follows an individualised care plan
* The journey should feel structured, positive, and achievable

#### 4. Personalised Care

Reinforce that every treatment plan is tailored specifically to the individual.

#### 5. Professional Reassurance

Patients should feel confident they are in expert hands and supported throughout their journey.

---

### **Design Direction**

* Use imagery that reflects calmness, progression, and wellness (e.g. pathways, nature, soft gradients)
* Avoid generic stock imagery
* **Only use original clinic images from website and social media**
* Prioritise white space and clarity
* Aim for a luxury spa/medical hybrid aesthetic

---

## **Content Structure (Page-by-Page)**

### **Front Cover**

* Clean, minimal, premium design
* Clinic branding

---

### **Page 1: Patient Case Summary**

**Title:** *Welcome to Fernwell Practice*

Thank you for choosing Fernwell Practice.

This booklet is designed to guide you through:

* What we found during your initial consultation
* Your personalised recommended treatment plan
* Your road to recovery
* Long-term wellness care
* Why we take the approach we do

---

### **Page 2: Your Care Journey**

**Stage 1: Your Initial Consultation**

Today we completed a comprehensive assessment of your health and function, including:

* Full case history and discussion of your symptoms and goals
* Orthopaedic and neurological testing
* Postural and movement assessment
* Initial treatment (where appropriate)

**What this tells us:**

* How your body is currently functioning
* Where areas of stress or dysfunction may be present
* The most appropriate and effective path forward for your care

---

### **Page 3: Your Suggested Treatment Plan**

Based on today’s findings, your recommended care plan is:

**______ treatments over ______ weeks**

This should be viewed alongside your *Road to Recovery* to help you understand what to expect.

We have also discussed:

* Expected timelines for improvement
* Available payment options

**After Treatment:**
It is common to feel different following treatment. This is a normal response as your body begins to adapt and respond.

We recommend:

* Staying well hydrated
* Allowing time for rest and recovery
* Avoiding overexertion if your body feels it needs it

---

### **Page 4: What to Expect Next**

Healing is not always linear—it is a process that occurs over time.

Your care will typically progress through the following stages:

* **Relief Care**
Focused on reducing discomfort and calming the body

* **Corrective Care**
Focused on addressing underlying issues and improving function
(This phase may include prescribed exercises)

* **Maintenance / Wellness Care**
Focused on sustaining progress, preventing recurrence, and supporting long-term health

---

### **Page 5: Understanding Chiropractic Care**

**What is Chiropractic?**
Chiropractic care focuses on the relationship between the spine, nervous system, and overall body function.

By improving spinal movement and alignment, chiropractic care helps support the nervous system, allowing the body to function and heal more effectively.

**About Fernwell Practice**
At Fernwell Practice, our approach is centred around personalised, patient-focused care. We aim to not only relieve symptoms but to address underlying causes and support long-term wellbeing.

---

### **Back Page**

* Clinic contact details
* Website
* Social media icons/handles

**Closing Message:**
“A healthier, stronger you—supported every step of the way.”

---

### **Deliverables**

* Print-ready PDF
* Editable source files

---

### **Additional Notes**

* The brochure should feel valuable and worth keeping
* Encourage long-term care in a subtle, non-pushy way
* Maintain clarity, readability, and strong visual hierarchy
* Balance professionalism with warmth and approachability

---

If you’d like, I can also turn this into **actual brochure copy (fully written, patient-facing text)** or help you refine it further for a designer.

Target Market(s)

Existing patients who want to feel better and look after themselves that is given after their initil consultation appointment

Industry/Entity Type

Chiropractic, wellness, health

Font styles to use
Other font styles liked:
• Montserrat or Lato

Colors
0094D4
00A9DD
6FCCEA
C7EBF8
E9F6FB
00AB8E
00BBA5
67D7C9
C6EFE9
E9F9F6
6B429C
8869AF
B7A5CE
E3DAEB
F3F0F8

Requirements
Must have
• my own photos, look premium wellness, be clear and simple to understand for patients journey or what to expect next and over time
Nice to have
• USe my social media/website for ideas
Should not have
• generic photos and images

```html
<!DOCTYPE html>
<html lang="en">
<head>
<meta charset="utf-8">
<title>Fernwell Practice – Patient Information Spread</title>
<link href="https://fonts.googleapis.com/css2?family=Montserrat:wght@400;500;600;700&family=Nothing+You+Could+Do&display=swap" rel="stylesheet">
<style>
:root{
  --backdrop:#3b4250;
  --paper:#ffffff;
  --ink:#1e1e24;
  --teal:#17a9a0;
  --teal-bright:#22b8b0;
  --teal-soft:#e2f6f5;
  --teal-line:#26b3ab;
  --slate-teal:#4d7c80;
  --purple:#8a6aa8;
  --purple-deep:#7a5c9c;
  --purple-band:#8a6a98;
  --lilac-soft:#efeaf3;
  --sky:#6fcce9;
}
*{box-sizing:border-box;margin:0;padding:0}
html,body{width:1200px;height:855px;overflow:hidden;background:var(--backdrop)}
body{position:relative;font-family:'Montserrat',sans-serif;color:var(--ink)}
.page{position:absolute;top:39px;width:547px;height:776px;background:var(--paper);overflow:hidden}
.page--left{left:42px}
.page--right{left:611px}
.abs{position:absolute}
.script{font-family:'Nothing You Could Do',cursive}

/* brand lockup */
.brand{position:absolute;text-align:center}
.brand__dot{width:80px;height:80px;border-radius:50%;background:var(--teal);margin:0 auto 14px}
.brand__name{font-weight:700;font-size:19px;color:var(--ink);letter-spacing:.3px;white-space:nowrap}

/* left page */
.hero-photo{left:227px;top:0;width:320px;height:306px;
  background:linear-gradient(100deg,rgba(255,255,255,1) 0%,rgba(255,255,255,0) 22%),
  linear-gradient(160deg,#f3e2a6 0%,#c9b27a 30%,#8a8a5c 60%,#4e5a3a 100%)}
.road-title{left:36px;top:204px;font-size:26px;font-weight:500;line-height:29px;letter-spacing:.2px}
.road-title strong{color:var(--teal);font-weight:700}
.road-sub{left:36px;top:264px;font-size:13.5px;line-height:17px}
.dash{left:36px;top:306px;width:175px;border-top:1.5px dashed var(--teal-line)}

.timeline{left:39px;top:330px;width:2px;height:360px;background:linear-gradient(var(--slate-teal),var(--teal),#bfe9e6,#dacde8,var(--purple-deep))}
.stage{position:absolute;left:0;width:230px;height:45px}
.stage__node{position:absolute;left:36px;top:5px;width:6px;height:6px;border-radius:50%}
.stage__icon{position:absolute;left:62px;top:-4px;width:26px;height:26px;border-radius:50%;display:flex;align-items:center;justify-content:center}
.stage__icon svg{width:15px;height:15px;fill:none;stroke:#fff;stroke-width:1.6;stroke-linecap:round;stroke-linejoin:round}
.stage__title{position:absolute;left:96px;top:0;font-size:10.5px;font-weight:600;letter-spacing:.2px}
.stage__text{position:absolute;left:96px;top:12px;font-size:9.3px;line-height:10.6px;white-space:nowrap}

.visit-title{left:292px;top:314px;font-size:25px;line-height:28px;font-weight:600;color:var(--purple)}
.visit-item{position:absolute;left:292px;width:250px;height:40px}
.visit-item__icon{position:absolute;left:0;top:0;width:32px;height:32px;border-radius:50%;background:var(--purple);display:flex;align-items:center;justify-content:center}
.visit-item__icon svg{width:18px;height:18px;fill:none;stroke:#fff;stroke-width:1.6;stroke-linecap:round;stroke-linejoin:round}
.visit-item__text{position:absolute;left:43px;top:-2px;font-size:9.4px;line-height:10.7px;white-space:nowrap}

.road-art{left:270px;top:490px;width:290px;height:280px;border-radius:60% 0 0 0;
  background:linear-gradient(200deg,rgba(111,204,234,.55) 0%,rgba(160,170,240,.45) 50%,rgba(183,165,206,.55) 100%)}
.road-note{left:358px;top:622px;font-size:14.5px;line-height:17px;color:var(--purple-deep);text-align:right;width:178px}

.band{position:absolute;left:0;bottom:0;width:100%;height:46px;background:var(--purple-band);display:flex;align-items:center;justify-content:center;color:#fff}
.band__url{font-size:17px;font-weight:600;letter-spacing:.3px}
.band__script{font-size:15px;letter-spacing:.5px}

/* right page */
.motto{left:242px;top:44px;font-size:30px;line-height:44px;color:var(--purple-deep)}
.motto span{display:block}
.motto span+span{padding-left:22px}
.plan-title{left:0;top:182px;width:100%;text-align:center;font-size:26px;font-weight:700;color:var(--teal);letter-spacing:.2px}
.plan-sub{left:0;top:208px;width:100%;text-align:center;font-size:13px}

.phases{left:53px;top:233px;width:442px;height:135px;border:1.5px solid var(--teal-line);border-radius:8px;display:flex;gap:8px;padding:6px 7px}
.phase{flex:1;background:var(--teal-soft);text-align:center;padding-top:6px;position:relative}
.phase svg.icon{width:38px;height:38px;fill:none;stroke:var(--teal);stroke-width:3;stroke-linecap:round;stroke-linejoin:round}
.phase__title{font-size:10.5px;font-weight:600;color:var(--teal);margin-top:9px}
.phase__text{font-size:7.4px;line-height:8.2px;margin-top:6px}
.chev{position:absolute;top:-7px;right:-14px;width:18px;height:135px;z-index:2}
.chev polyline{fill:none;stroke:var(--teal-line);stroke-width:1.5}

.note{left:59px;top:381px;width:428px;height:46px;background:var(--lilac-soft);border-radius:3px;text-align:center;font-size:9.8px;line-height:10.8px;padding-top:7px}

.easy-title{left:58px;top:440px;font-size:15px;font-weight:700;color:var(--teal);letter-spacing:.2px}
.easy-item{position:absolute;left:59px;width:180px;height:40px}
.easy-item__icon{position:absolute;left:0;top:0;width:32px;height:32px;border-radius:50%;background:var(--teal);display:flex;align-items:center;justify-content:center}
.easy-item__icon svg{width:18px;height:18px;fill:none;stroke:#fff;stroke-width:1.6;stroke-linecap:round;stroke-linejoin:round}
.easy-item__title{position:absolute;left:42px;top:-2px;font-size:9.8px;font-weight:600;color:var(--teal);white-space:nowrap}
.easy-item__text{position:absolute;left:42px;top:11px;font-size:7.4px;line-height:10.6px;white-space:nowrap}

.philosophy{left:242px;top:434px;width:245px;height:93px;background:var(--lilac-soft);border-radius:6px 6px 0 0;padding:6px 12px}
.box-title{font-size:15px;font-weight:700;letter-spacing:.2px}
.philosophy .box-title{color:var(--purple)}
.philosophy p{font-size:9.6px;line-height:10.6px;margin-top:7px}
.values{left:242px;top:529px;width:245px;height:109px;background:var(--purple-band);border-radius:0 0 6px 6px;padding:4px 12px;color:#fff}
.values ul{list-style:none;margin-top:2px}
.values li{font-size:9.6px;line-height:16.8px;display:flex;align-items:center;gap:6px}
.values li svg{width:9px;height:9px;fill:none;stroke:#67d7c9;stroke-width:2.4;stroke-linecap:round;stroke-linejoin:round}

.commit{left:59px;top:649px;width:428px;height:70px;background:var(--teal-soft);border-radius:3px}
.commit svg{position:absolute;fill:none;stroke:var(--teal);stroke-width:2.4;stroke-linecap:round;stroke-linejoin:round}
.commit__col{position:absolute;top:13px}
.commit__head{font-size:9px;line-height:10.8px;font-weight:600;color:var(--teal);letter-spacing:.2px}
.commit__body{font-size:9.6px;line-height:10.8px;margin-top:5px;white-space:nowrap}
</style>
</head>
<body>

<!-- LEFT PAGE -->
<section class="page page--left">
  <div class="brand" style="left:40px;top:40px;width:180px">
    <div class="brand__dot"></div>
    <div class="brand__name">Fernwell Practice</div>
  </div>

  <div class="hero-photo abs" role="img" aria-label="Photo of a woman jogging through a sunlit woodland"></div>

  <h1 class="road-title abs">YOUR ROAD<br><strong>TO RECOVERY</strong></h1>
  <p class="road-sub abs">We’re with you at every step<br>of the way</p>
  <div class="dash abs"></div>

  <div class="timeline abs"></div>
  <div class="abs" style="left:0;top:330px;width:260px;height:400px">
    <div class="stage" style="top:0">
      <span class="stage__node" style="background:var(--slate-teal)"></span>
      <span class="stage__icon" style="background:var(--slate-teal)"><svg viewBox="0 0 20 20"><circle cx="10" cy="10" r="4"/><path d="M10 2v2M10 16v2M2 10h2M16 10h2M4.3 4.3l1.4 1.4M14.3 14.3l1.4 1.4M4.3 15.7l1.4-1.4M14.3 5.7l1.4-1.4"/></svg></span>
      <span class="stage__title" style="color:var(--slate-teal)">OPTIMISING</span>
      <span class="stage__text">Performing at your best<br>every day.</span>
    </div>
    <div class="stage" style="top:45px">
      <span class="stage__node" style="background:var(--teal)"></span>
      <span class="stage__icon" style="background:var(--teal)"><svg viewBox="0 0 20 20"><circle cx="8" cy="7" r="3"/><path d="M3 16c0-3 2-5 5-5s5 2 5 5M15 6v5M12.5 8.5h5"/></svg></span>
      <span class="stage__title" style="color:var(--teal)">ENHANCING</span>
      <span class="stage__text">Building on progress<br>and wellbeing.</span>
    </div>
    <div class="stage" style="top:90px">
      <span class="stage__node" style="background:var(--teal-bright)"></span>
      <span class="stage__icon" style="background:var(--teal-bright)"><svg viewBox="0 0 20 20"><rect x="4" y="4" width="12" height="12" rx="1"/><path d="M7 10l2 2 5-6"/></svg></span>
      <span class="stage__title" style="color:var(--teal-bright)">CORRECTING</span>
      <span class="stage__text">Addressing the cause,<br>not just the symptoms.</span>
    </div>
    <div class="stage" style="top:135px">
      <span class="stage__node" style="background:#8fdcd6"></span>
      <span class="stage__icon" style="background:#9fe0db"><svg viewBox="0 0 20 20"><path d="M10 3l6 2v5c0 4-3 6-6 7-3-1-6-3-6-7V5z"/><path d="M7.5 10l2 2 3-4"/></svg></span>
      <span class="stage__title" style="color:#7fd6d0">STABILISING</span>
      <span class="stage__text">Restoring balance and<br>building resiliennce.</span>
    </div>
    <div class="stage" style="top:180px">
      <span class="stage__node" style="background:#bfe6f2"></span>
      <span class="stage__icon" style="background:#e3daeb"><svg viewBox="0 0 20 20"><path d="M2 10h16M5 7v6M15 7v6M7 8v4M13 8v4"/></svg></span>
      <span class="stage__title" style="color:#d8c8e4">STRENGTHENING</span>
      <span class="stage__text">Supporting strength,<br>confidence and movement.</span>
    </div>
    <div class="stage" style="top:225px">
      <span class="stage__node" style="background:#cdbde0"></span>
      <span class="stage__icon" style="background:#dccfe8"><svg viewBox="0 0 20 20"><path d="M10 16s-6-3.5-6-8a3 3 0 0 1 6-1 3 3 0 0 1 6 1c0 4.5-6 8-6 8z"/></svg></span>
      <span class="stage__title" style="color:#c8b4dc">HEALING</span>
      <span class="stage__text">Reducing pain, improving<br>function, feeling better.</span>
    </div>
    <div class="stage" style="top:270px">
      <span class="stage__node" style="background:#b49ad0"></span>
      <span class="stage__icon" style="background:#c4aedb"><svg viewBox="0 0 20 20"><path d="M4 4v12h12M6 13l3-4 3 2 4-5"/></svg></span>
      <span class="stage__title" style="color:#b49ad0">RECOVERING</span>
      <span class="stage__text">Moving forward with<br>more freedom.</span>
    </div>
    <div class="stage" style="top:315px">
      <span class="stage__node" style="background:#9a7fc0"></span>
      <span class="stage__icon" style="background:#9a7fc0"><svg viewBox="0 0 20 20"><path d="M10 3l2 4.5 5 .5-3.8 3.3 1.2 4.9L10 13.6 5.6 16.2l1.2-4.9L3 8l5-.5z" fill="#fff"/></svg></span>
      <span class="stage__title" style="color:#9a7fc0">IMPROVING</span>
      <span class="stage__text">Living well, doing more<br>of what your love.</span>
    </div>
    <div class="stage" style="top:360px">
      <span class="stage__node" style="background:var(--purple-deep)"></span>
      <span class="stage__icon" style="background:var(--purple-deep)"><svg viewBox="0 0 20 20"><circle cx="10" cy="6" r="2.5"/><path d="M5 16l3-6h4l3 6"/></svg></span>
      <span class="stage__title" style="color:var(--purple-deep)">SUFFERING</span>
      <span class="stage__text">Pain and limitations<br>impact your daily life.</span>
    </div>
  </div>

  <h2 class="visit-title abs">EXPLAINING YOUR<br>FIRST VISIT</h2>
  <div class="visit-item" style="top:374px">
    <span class="visit-item__icon"><svg viewBox="0 0 20 20"><path d="M4 14l-1 3 4-1.5c1 .4 2 .5 3 .5 4 0 7-2.7 7-6s-3-6-7-6-7 2.7-7 6c0 1.5.4 2.8 1 4z"/></svg></span>
    <span class="visit-item__text">Today, we listened to your story,<br>understood your concerns and<br>performed a thorough assessement.</span>
  </div>
  <div class="visit-item" style="top:416px">
    <span class="visit-item__icon"><svg viewBox="0 0 20 20"><circle cx="8.5" cy="8.5" r="5"/><path d="M12.5 12.5l4.5 4.5"/></svg></span>
    <span class="visit-item__text">We identified the things that may<br>be contributing to your pain or<br>discomfort.</span>
  </div>
  <div class="visit-item" style="top:458px">
    <span class="visit-item__icon"><svg viewBox="0 0 20 20"><rect x="5" y="4" width="10" height="13" rx="1"/><path d="M8 3h4v2H8zM7.5 9h5M7.5 12h5M7.5 15h3"/></svg></span>
    <span class="visit-item__text">We explained our findings<br>in clear, simple terms.</span>
  </div>
  <div class="visit-item" style="top:499px">
    <span class="visit-item__icon"><svg viewBox="0 0 20 20"><path d="M10 16s-6-3.5-6-8a3 3 0 0 1 6-1 3 3 0 0 1 6 1c0 4.5-6 8-6 8z"/></svg></span>
    <span class="visit-item__text">We discussed your goals and what<br>you would like to achieve.</span>
  </div>
  <div class="visit-item" style="top:541px">
    <span class="visit-item__icon"><svg viewBox="0 0 20 20"><path d="M6 4c1.5 0 2 1.5 2 4s-.5 4-2 4-2-1.5-2-4 .5-4 2-4zM14 6c1.5 0 2 1.5 2 4s-.5 4-2 4-2-1.5-2-4 .5-4 2-4zM5 14h2v2H5zM13 16h2v2h-2z"/></svg></span>
    <span class="visit-item__text">We recommended a plan<br>designed specifically<br>for you.</span>
  </div>

  <div class="road-art abs" role="img" aria-label="Illustration of a winding path rising from lilac to sky blue"></div>
  <p class="road-note abs script">You’ve taken the<br>first step. We’ll guide<br>you the rest of the way.</p>

  <footer class="band"><span class="band__url">www.fernwellpractice-wells.com</span></footer>
</section>

<!-- RIGHT PAGE -->
<section class="page page--right">
  <div class="brand" style="left:30px;top:30px;width:185px">
    <div class="brand__dot"></div>
    <div class="brand__name">Fernwell Practice</div>
  </div>

  <p class="motto abs script"><span>You. Stronger.</span><span>Healthier. Happier.</span></p>

  <h2 class="plan-title abs">YOUR PERSONALISED CARE PLAN</h2>
  <p class="plan-sub abs">Every body is different. You care plan is designed around you</p>

  <div class="phases abs">
    <div class="phase">
      <svg class="icon" viewBox="0 0 40 40"><circle cx="19" cy="21" r="14"/><circle cx="19" cy="21" r="8"/><circle cx="19" cy="21" r="2.5"/><path d="M19 21L33 7M29 5l4 2 2 4"/></svg>
      <div class="phase__title">CORRECTION</div>
      <div class="phase__text">We focus on reducing<br>pain and improving<br>movement.<br>You’ll start to feel the<br>change</div>
      <svg class="chev" viewBox="0 0 18 135"><polyline points="2,0 16,30 2,135"/></svg>
    </div>
    <div class="phase">
      <svg class="icon" viewBox="0 0 40 40"><path d="M20 4l13 5v10c0 9-6 14-13 17-7-3-13-8-13-17V9z"/><path d="M14 20l4 4 8-8"/></svg>
      <div class="phase__title">STABILISATION</div>
      <div class="phase__text">We build stability<br>and restore<br>balance.<br>Your body starts to<br>hold progress.</div>
      <svg class="chev" viewBox="0 0 18 135"><polyline points="2,0 16,30 2,135"/></svg>
    </div>
    <div class="phase">
      <svg class="icon" viewBox="0 0 40 40"><path d="M4 20h32M9 13v14M31 13v14M14 11v18M26 11v18"/></svg>
      <div class="phase__title">STRENGTHENING</div>
      <div class="phase__text">We improve strenght,<br>resilience and<br>confidence.<br>You move better<br>and feel stronger.</div>
      <svg class="chev" viewBox="0 0 18 135"><polyline points="2,0 16,30 2,135"/></svg>
    </div>
    <div class="phase">
      <svg class="icon" viewBox="0 0 40 40"><circle cx="18" cy="6" r="3.5" fill="var(--teal)"/><path d="M6 10l12 6 12-6M18 16l-2 10-5 10M16 26l8 10"/><path d="M31 22l2 4 4 .5-3 2.5 1 4-4-2-4 2 1-4-3-2.5 4-.5z" fill="var(--teal)"/></svg>
      <div class="phase__title">OPTIMISING</div>
      <div class="phase__text" style="margin-top:12px">We support you to<br>perform at you best –<br>in work, life and<br>everything in between.</div>
    </div>
  </div>

  <p class="note abs">This plan may include chiropractic care, soft tissue therapy, exercise,<br>posture and lifestyle advice. Well review your progress regularly<br>and adjust as needed.</p>

  <h3 class="easy-title abs">MAKING CARE EASY</h3>
  <div class="easy-item" style="top:484px">
    <span class="easy-item__icon"><svg viewBox="0 0 20 20"><rect x="3.5" y="4.5" width="13" height="12" rx="1.5"/><path d="M3.5 8h13M7 3v3M13 3v3M7 11h1M10 11h1M13 11h1M7 14h1M10 14h1"/></svg></span>
    <span class="easy-item__title">We agree a plan together</span>
    <span class="easy-item__text">You’ll know how often to attend<br>and why it matters.</span>
  </div>
  <div class="easy-item" style="top:527px">
    <span class="easy-item__icon"><svg viewBox="0 0 20 20"><rect x="5" y="4" width="10" height="13" rx="1"/><path d="M8 3h4v2H8zM7.5 9h5M7.5 12h5M7.5 15h3"/></svg></span>
    <span class="easy-item__title">Clear steps. Clear goals.</span>
    <span class="easy-item__text">We break it down so it’s easy<br>to follow.</span>
  </div>
  <div class="easy-item" style="top:570px">
    <span class="easy-item__icon"><svg viewBox="0 0 20 20"><circle cx="10" cy="7" r="3.5"/><path d="M4 17c0-3.5 2.5-5.5 6-5.5s6 2 6 5.5z"/></svg></span>
    <span class="easy-item__title">You’re never alone</span>
    <span class="easy-item__text">We’re here to support, guide<br>and celebrate your progress.</span>
  </div>
  <div class="easy-item" style="top:613px">
    <span class="easy-item__icon"><svg viewBox="0 0 20 20"><path d="M4 4v12h12M6 13l3-4 3 2 4-5M13 6h3v3"/></svg></span>
    <span class="easy-item__title">Track your progress</span>
    <span class="easy-item__text">We measure what matters<br>so you can see your results.</span>
  </div>

  <div class="philosophy abs">
    <h3 class="box-title">OUR PHILOSOPHY</h3>
    <p>We believe your body has an incredible ability<br>to heal when it’s supported the right way.</p>
    <p>Our mission is to help you move well, feel well<br>and live well – naturally.</p>
  </div>
  <div class="values abs">
    <h3 class="box-title">THE VALUE WE BRING</h3>
    <ul>
      <li><svg viewBox="0 0 10 10"><path d="M1 5l3 3 5-6"/></svg>Experts care you can trust</li>
      <li><svg viewBox="0 0 10 10"><path d="M1 5l3 3 5-6"/></svg>Personalised plans, not one-size-fits-all</li>
      <li><svg viewBox="0 0 10 10"><path d="M1 5l3 3 5-6"/></svg>Evidence-informed, results-focused</li>
      <li><svg viewBox="0 0 10 10"><path d="M1 5l3 3 5-6"/></svg>A warm, welcoming environment</li>
      <li><svg viewBox="0 0 10 10"><path d="M1 5l3 3 5-6"/></svg>We care about your long-term wellbeing</li>
    </ul>
  </div>

  <div class="commit abs">
    <svg viewBox="0 0 56 50" style="left:6px;top:10px;width:56px;height:50px"><circle cx="28" cy="9" r="6"/><circle cx="10" cy="16" r="4.5"/><circle cx="46" cy="16" r="4.5"/><path d="M18 30c1-7 5-10 10-10s9 3 10 10M3 32c0-6 3-9 7-9M53 32c0-6-3-9-7-9"/><path d="M28 47s-8-4.5-8-9.5a4 4 0 0 1 8-1.5 4 4 0 0 1 8 1.5c0 5-8 9.5-8 9.5z" fill="var(--teal)"/></svg>
    <div class="commit__col" style="left:67px">
      <div class="commit__head">BETTER UNDERSTANDING<br>BETTER RESULTS.</div>
      <div class="commit__body">Understanding you plan helps<br>you get the most from you care.</div>
    </div>
    <div class="commit__col" style="left:226px">
      <div class="commit__head">YOUR COMMINTMENT.<br>OUR COMMITMENT</div>
      <div class="commit__body">Together, we’ll help you reach<br>your goals and keep you well</div>
    </div>
    <svg viewBox="0 0 52 36" style="left:372px;top:16px;width:52px;height:36px"><path d="M2 6l8-3 6 14-8 3zM50 6l-8-3-6 14 8 3z"/><path d="M16 9l8-3 6 3 6-1M14 18l10 10c1.5 1.5 3 0 2-1.5M20 22l7 6c1.5 1.5 3 0 2-1.5M24 18l7 6c1.5 1.5 3 0 2-1.5M36 17l-6-6-6 4"/></svg>
  </div>

  <footer class="band"><span class="band__script script">We’re here for you – every step of the way.</span></footer>
</section>

</body>
</html>
```